An Engineering book catering oil and gas engineering students and professionals

I need a logo for the cover page of the book. I suggest you watch on vidstreamo the drilling for oil and gas video not more than 10 mins. Once you have watched it then you can go ahead and watch the video on Managed Pressure Drilling Technique. I am currently the only person in the industry who is teaching the most comprehensive course on this technique hence the book on the same topic which will compliment my teachings to my attendees.
While you are designing the logo keep oil and gas drilling, high pressure , high temperature, pressure gauges, reservoir rock where oil and gas are trapped. if you like I can also put some pictures here and you can have a look.

Managed pressure drilling is all about balancing the pressure with the pressure that is inside the reservoir rock. I will try to attach some pictures later. With the light fluid inside the well we apply pressure from surface that make the pressure inside the well equal to the formation or reservoir rock pressure.

The book design has to portray an engineering book cover so try to avoid too much colour please. My name is Rafiq (Raf) Dorvani therefore the book should have my name on the stem of the book. At the front the design should be elegant with an easy and readable title of the book.

The name of the book is "Borehole Equilibrium Control" (Engineering & Operations). Plz avoid rig or pump jack pictures it is too old. Work with pressure gauge, pressure or balancing the pressure etc. You can also place words like BHCP, ECD, ESD, DIF. IME, WC Matrix, RCD, ACM, RPDS, NSD, CT. Please dont put pictures of drill machines, oil and gas drilling is not done with drill machines :). Moreover, the book size will be smaller than the A4 page meaning Length 24 inches width of 17 inches. See what you come up with and we go from there

```html
<!DOCTYPE html>
<html lang="en">
<head>
<meta charset="UTF-8">
<title>Borehole Equilibrium Control – Book Cover</title>
<link rel="stylesheet" href="https://fonts.googleapis.com/css2?family=Bebas+Neue&family=Montserrat:wght@400;600;800&display=swap">
<style>
  :root {
    --orange: #f37021;
    --ink: #333333;
    --paper: #ffffff;
    --page-bg: #ffffff;
    --body-text: #3a3a3a;
    --rule: #e4e4e4;
  }
  * { margin: 0; padding: 0; box-sizing: border-box; }
  html, body {
    width: 756px; height: 1200px; overflow: hidden;
    background: var(--page-bg);
  }
  .cover-wrap {
    position: absolute;
    left: 28px; top: 362px;
    width: 700px; height: 475px;
    display: flex;
    background: var(--paper);
    box-shadow: 0 6px 22px rgba(0,0,0,0.28);
  }
  .panel { position: relative; height: 100%; background: var(--paper); }
  .back { width: 328px; }
  .spine { width: 51px; border-left: 1px solid var(--rule); }
  .front { width: 321px; }

  .band {
    position: absolute; left: 0; right: 0; bottom: 0;
    height: 47px; background: var(--orange);
  }

  .title-block { position: absolute; width: 224px; }
  .back .title-block { left: 47px; top: 34px; }
  .front .title-block { left: 45px; top: 34px; }

  .title-top {
    font-family: "Bebas Neue", sans-serif;
    font-size: 31px; line-height: 0.9;
    color: var(--ink); white-space: nowrap;
  }
  .title-main {
    font-family: "Bebas Neue", sans-serif;
    font-size: 80px; line-height: 0.8;
    color: var(--orange); letter-spacing: 0.5px;
    margin-top: 3px;
  }
  .title-sub {
    font-family: "Montserrat", sans-serif;
    font-weight: 600; font-size: 14.2px;
    color: var(--ink); white-space: nowrap;
    margin-top: 4px;
  }

  .blurb {
    position: absolute; left: 47px; width: 222px;
    font-family: "Montserrat", sans-serif;
    font-size: 7.4px; line-height: 8.7px;
    color: var(--body-text); text-align: justify;
  }
  .blurb p + p { margin-top: 8.7px; }
  .blurb-intro { top: 154px; }
  .author-heading {
    position: absolute; left: 47px; top: 287px;
    font-family: "Bebas Neue", sans-serif;
    font-weight: 400; font-size: 20px; line-height: 1;
    color: var(--ink);
  }
  .blurb-bio { top: 317px; }

  .isbn-box {
    position: absolute; left: 172px; top: 407px;
    width: 128px; height: 53px;
    background: var(--paper); border: 1px solid #222;
  }

  .spine-name {
    position: absolute; left: 50%; top: 36px;
    transform: translateX(-50%);
    writing-mode: vertical-rl;
    font-family: "Montserrat", sans-serif;
    font-weight: 800; font-size: 31px; line-height: 1;
    color: var(--ink); white-space: nowrap;
  }
  .spine-name .first { color: var(--orange); }

  .emblem {
    position: absolute; left: 78px; top: 166px;
    width: 182px; height: 226px;
    border-radius: 50% 50% 46% 46%;
    background: radial-gradient(circle at 50% 60%, var(--ink) 0%, #555 38%, var(--orange) 62%, rgba(243,112,33,0.15) 78%, transparent 80%);
  }

  .front-name {
    position: absolute; left: 0; right: 0; bottom: 0;
    height: 47px; line-height: 50px; text-align: center;
    font-family: "Bebas Neue", sans-serif;
    font-size: 31px; color: var(--paper);
  }
</style>
</head>
<body>
  <div class="cover-wrap">
    <section class="panel back">
      <div class="band"></div>
      <div class="title-block">
        <div class="title-top">BOREHOLE EQUILIBRIUM</div>
        <div class="title-main">CONTROL</div>
        <div class="title-sub">ENGINEERING &amp; OPERATIONS</div>
      </div>
      <div class="blurb blurb-intro">
        <p>Lorem Ipsum is simply dummy text of the printing and typesetting industry. Lorem Ipsum has been the industry's standard dummy text ever since the 1500s, when an unknown printer took a galley of type and scrambled it to make a type specimen book. It has survived not only five centuries, but also the leap into electronic typesetting, remaining essentially unchanged. It was popularised in the 1960s with the release of Tessarine sheets containing Lorem Ipsum passages, and more recently with desktop publishing software like Quillset Layout including versions of Lorem Ipsum.</p>
        <p>Lorem Ipsum is simply dummy text of the printing and typesetting industry.</p>
      </div>
      <h2 class="author-heading">RAFIQ (RAF) DORVANI</h2>
      <div class="blurb blurb-bio">
        <p>Lorem Ipsum is simply dummy text of the printing and typesetting industry. Lorem Ipsum has been the industry's standard dummy text ever since the 1500s, when an unknown printer took a galley of type and scrambled it to make a type specimen book. It has survived not only five centuries, but also the leap into electronic typesetting, remaining essentially unchanged. It was popularised in the 1960s with the release of Tessarine sheets containing Lorem Ipsum passages, and more recently with desktop publishing software like Quillset Layout including versions of Lorem Ipsum.</p>
      </div>
      <div class="isbn-box"></div>
    </section>

    <section class="panel spine">
      <div class="spine-name"><span class="first">RAFIQ</span> (RAF) DORVANI</div>
    </section>

    <section class="panel front">
      <div class="title-block">
        <div class="title-top">BOREHOLE EQUILIBRIUM</div>
        <div class="title-main">CONTROL</div>
        <div class="title-sub">ENGINEERING &amp; OPERATIONS</div>
      </div>
      <div class="emblem" role="img" aria-label="Cover emblem: orange gear ring framing a dark well structure over mountains with an orange flame drop"></div>
      <div class="band"></div>
      <div class="front-name">RAFIQ (RAF) DORVANI</div>
    </section>
  </div>
</body>
</html>
```